Music Web page

We are the largest community of artists, bands, podcasters and creators of music. We need web pages design.

What we need:
1. Registration form page
- Full Name
- Username
- Email Address
- Password
- Captcha

2. Songs/Artists gallery page
- Cover
- Simple MP3 Player
- Share | Like | Comments

3. Contact us page
- Name
- Email
- Phone
- Message
- Captcha

Send me a registration form first, If it makes me "hands on the air" , then I will continue to work with you.

Industry/Entity Type

Artists

Colors
eb1f27

Requirements
Nice to have
• Dark / black color for background

```html
<!DOCTYPE html>
<html lang="en">
<head>
<meta charset="utf-8">
<title>Soundline – One Page Web Form</title>
<link href="https://fonts.googleapis.com/css2?family=Lato:wght@300;400;700;900&display=swap" rel="stylesheet">
<style>
:root{
  --stage:#323843;
  --red:#eb1f27;
  --black:#000;
  --charcoal:#1b1b1b;
  --wine:#2a0000;
  --white:#fff;
  --grey:#9a9a9a;
  --btn:#3a3a3a;
  --map:#2b2b2b;
}
*{box-sizing:border-box;margin:0;padding:0}
html,body{width:1200px;height:853px;overflow:hidden}
body{background:var(--stage);font-family:'Lato',sans-serif;color:var(--white);position:relative}
.page{position:absolute;left:450px;top:0;width:300px;height:853px;display:flex;flex-direction:column;box-shadow:0 0 30px rgba(0,0,0,.4)}
.page>*{flex:none}
.topbar{height:13px;background:var(--charcoal);display:flex;justify-content:flex-end;align-items:center;gap:3px;padding:0 28px}
.social{width:6px;height:6px;background:#666;border-radius:1px}
.nav{height:20px;background:var(--red);display:flex;align-items:center;padding:0 30px;border-bottom:2px solid var(--black)}
.brand{font-weight:900;font-size:10px;color:var(--black);letter-spacing:-.2px}
.menu{margin-left:auto;display:flex;gap:5px;font-size:3.6px;font-weight:700;text-transform:uppercase}
.hero{height:95px;background:var(--black);text-align:center;padding-top:16px}
h1,h2{font-weight:900;letter-spacing:-.3px}
.hero h1{font-size:18px}
.lead{font-size:7px;margin-top:2px}
.btn{display:inline-block;background:var(--btn);color:#ddd;border-radius:8px;font-size:5px;padding:3px 8px;margin-top:10px;box-shadow:0 1px 3px rgba(0,0,0,.5)}
.register{height:135px;background:var(--red);display:flex;padding:18px 16px 0 30px;gap:14px}
.form{width:112px;display:flex;flex-direction:column;align-items:center}
.form-title{font-size:4px;margin-bottom:2px}
.field{width:112px;height:7px;background:var(--white);margin-bottom:3px;color:#999;font-size:3.5px;padding-left:2px;line-height:7px}
.captcha{font-size:3.5px;margin-top:1px}
.captcha-box{width:18px;height:5px;background:var(--white);margin:1px 0;color:#333;font-size:3.5px;text-align:center;line-height:5px}
.send{background:var(--btn);border-radius:6px;font-size:4px;padding:2px 5px;margin-top:5px}
.intro{flex:1;text-align:center;padding-top:8px}
.intro h2{font-size:14px}
.intro p{font-size:5px;line-height:1.6;margin-top:4px}
.intro .btn{margin-top:4px;font-size:4px;padding:2px 5px}
.music{height:132px;background:var(--charcoal);text-align:center;padding-top:14px}
.music h2{font-size:15px}
.values{display:flex;justify-content:center;gap:26px;margin-top:12px}
.value{width:54px}
.badge{width:38px;height:38px;border-radius:50%;margin:0 auto 4px}
.badge.universal{background:radial-gradient(circle,#e99a84,#e0634c)}
.badge.digital{background:radial-gradient(circle,#bfe4e8,#5bbfc7)}
.badge.love{background:radial-gradient(circle,#f7d07a,#f0b64a)}
.value h3{font-size:5px;font-weight:700}
.value p{font-size:3.4px;color:#bbb;line-height:1.4;margin-top:1px}
.special{height:121px;background:var(--black);display:flex;align-items:center;padding:0 22px 0 26px}
.special-text{width:120px;text-align:center}
.special-text h2{font-size:14px;color:var(--red);line-height:1}
.special-text p{font-size:4px;margin-top:4px}
.chart{margin-left:auto}
.contact{height:112px;background:var(--wine);display:flex;padding:14px 16px 0 24px;gap:10px}
.contact-text{width:130px;text-align:center}
.contact-text h2{font-size:14px}
.contact-text p{font-size:4px;line-height:1.5;margin-top:3px}
.details{font-size:4px;line-height:1.6;margin-top:5px}
.details svg{width:4px;height:4px;vertical-align:-.5px;margin-right:1px}
.video{width:108px;height:62px;border:2px solid var(--white);margin-top:12px;background:linear-gradient(160deg,#6a6a6a,#1e1e1e 70%)}
.location{height:71px;background:var(--black);text-align:center;padding-top:20px}
.location h2{font-size:16px}
.location p{font-size:6px;margin-top:2px}
.map{height:92px;background:linear-gradient(135deg,#333,var(--map) 60%,#242424)}
.footer{height:62px;background:var(--charcoal);display:flex;flex-direction:column;align-items:center;padding-top:16px}
.footer .socials{display:flex;gap:7px}
.footer .social{width:9px;height:9px;border-radius:50%;background:#444}
.footer .menu{margin:7px 0 0;gap:4px;font-size:3px;font-weight:400}
</style>
</head>
<body>
<main class="page">
  <div class="topbar"><span class="social"></span><span class="social"></span><span class="social"></span><span class="social"></span></div>
  <nav class="nav">
    <span class="brand">Soundline</span>
    <div class="menu"><span>Home</span><span>Registration Form</span><span>Our Specialisation</span><span>Contact Us</span><span>Map</span></div>
  </nav>
  <header class="hero">
    <h1>Sample Form Page</h1>
    <p class="lead">We look forward to your feedback.</p>
    <span class="btn">Scroll Down</span>
  </header>
  <section class="register">
    <div class="form">
      <div class="form-title">Registration Form</div>
      <div class="field">First Name</div>
      <div class="field">Last Name</div>
      <div class="field">Username</div>
      <div class="field">Email Address</div>
      <div class="field">Password</div>
      <div class="captcha">Answer this simple Captcha</div>
      <div class="captcha-box">2 + 3 =</div>
      <div class="captcha">Type to Check</div>
      <div class="field"></div>
      <span class="send">Send</span>
    </div>
    <div class="intro">
      <h2>Your Form.</h2>
      <p>We thought it would be great if we could also showcase a little of our skills, scroll down to see what else we can do.</p>
      <span class="btn">Learn More</span>
    </div>
  </section>
  <section class="music">
    <h2>Music is...</h2>
    <div class="values">
      <div class="value"><div class="badge universal" role="img" aria-label="Globe illustration"></div><h3>Universal.</h3><p>Shared by every listener, on every corner of the world.</p></div>
      <div class="value"><div class="badge digital" role="img" aria-label="Computer screen illustration"></div><h3>Digital.</h3><p>Streamed, mixed and passed along in a single tap.</p></div>
      <div class="value"><div class="badge love" role="img" aria-label="Heart illustration"></div><h3>Love.</h3><p>Felt deep in the chest, long after the last note.</p></div>
    </div>
  </section>
  <section class="special">
    <div class="special-text">
      <h2>Our<br>Specialisation.</h2>
      <p>Roll over to see what the sections represents.</p>
    </div>
    <svg class="chart" width="90" height="90" viewBox="0 0 90 90" aria-label="Specialisation breakdown chart">
      <g transform="rotate(-90 45 45)" fill="none" stroke-width="22">
        <circle cx="45" cy="45" r="30" stroke="#5a0000" stroke-dasharray="56 189"/>
        <circle cx="45" cy="45" r="30" stroke="#ff6b6b" stroke-dasharray="40 189" stroke-dashoffset="-56"/>
        <circle cx="45" cy="45" r="30" stroke="#e8323a" stroke-dasharray="36 189" stroke-dashoffset="-96"/>
        <circle cx="45" cy="45" r="30" stroke="#b3121a" stroke-dasharray="26 189" stroke-dashoffset="-132"/>
        <circle cx="45" cy="45" r="30" stroke="#7a0a0a" stroke-dasharray="31 189" stroke-dashoffset="-158"/>
      </g>
    </svg>
  </section>
  <section class="contact">
    <div class="contact-text">
      <h2>Contact Us.</h2>
      <p>Feel free to email us, phone us, smoke signal us, carrier pigeon us, or visit us. You can find us using our nifty map (just scroll down a bit).</p>
      <div class="details">
        <div><svg viewBox="0 0 10 10"><rect x="0" y="2" width="10" height="7" fill="#fff"/><path d="M0 2 5 6 10 2" stroke="#2a0000" fill="none"/></svg>info@northbeam.example</div>
        <div><svg viewBox="0 0 10 10"><path d="M2 0 4 3 3 4Q4 6 6 7L7 6 10 8 8 10Q1 9 0 2Z" fill="#fff"/></svg>+65.5550.0142</div>
        <div><svg viewBox="0 0 10 10"><path d="M5 0A3.5 3.5 0 0 0 1.5 3.5C1.5 6 5 10 5 10S8.5 6 8.5 3.5A3.5 3.5 0 0 0 5 0Z" fill="#fff"/></svg>12 Harbour Road, Unit 03-04,<br>Harbour Point, Singapore 000000</div>
      </div>
    </div>
    <div class="video" role="img" aria-label="Agency showreel video still, dark splash imagery"></div>
  </section>
  <section class="location">
    <h2>Location.</h2>
    <p>Let's meet up and discuss business-y things.</p>
  </section>
  <div class="map" role="img" aria-label="Dark street map of the office area"></div>
  <footer class="footer">
    <div class="socials"><span class="social"></span><span class="social"></span><span class="social"></span><span class="social"></span></div>
    <div class="menu"><span>Home</span><span>Registration Form</span><span>Our Specialisation</span><span>Contact Us</span><span>Map</span></div>
  </footer>
</main>
</body>
</html>
```